Poster Art for Feature Film

We need a poster art for a feature film called Hallway Sparks. It is a family film that focuses on dealing with the pressures of conformity in high school. Has a well known cast that you can look up on FLMX under Hallway Sparks 2013 and a Facebook fan page under Hallwaysparksfilm, as well as a twitter account under hallwaysparksfilm. It is a positive, hopeful story with a target market in the 9-15 year old range. Film deals with transformation so I see that in the poster as well as key cast members. We can discuss different ways to express the theme. Would be used for web site, Facebook, twitter, and possibly film posters and media packets. This is not the final poster art for the film but an initial way for us to express what the film is about. Successful artist will be strongly considered for final film poster art.

thank you all for the wonderful submissions.   this was a very tough choice and we appreciate your patience!

Target Market(s)

9 to 14 year old kids.

Industry/Entity Type

School

Requirements
Must have
• appealing to family particularly kids. show transformation from being alone to being part of a group. Being guarded to open.
Nice to have
• art would would appeal to both boys and girls.
Should not have
• no sexual inuendo, content,

```html
<!DOCTYPE html>
<html lang="en">
<head>
<meta charset="utf-8">
<title>Hallway Sparks – Poster</title>
<link rel="stylesheet" href="https://fonts.googleapis.com/css2?family=Graduate&family=Archivo:wght@700;800&family=Over+the+Rainbow&display=swap">
<style>
  :root {
    --paper: #e4e8ea;
    --ink: #111217;
    --pink: #e8197f;
    --blue: #1b8fd6;
    --white: #ffffff;
    --tag-bg: rgba(236, 236, 226, 0.88);
    --chalk: #bcd3ee;
  }
  * { margin: 0; padding: 0; box-sizing: border-box; }
  html, body { width: 902px; height: 1200px; overflow: hidden; background: var(--paper); }
  .poster { position: relative; width: 902px; height: 1200px; overflow: hidden; background: var(--paper); }
  .collage { position: absolute; inset: 0; }

  .title {
    position: absolute; left: 40px; top: 392px; width: 822px;
    display: flex; flex-direction: column; gap: 8px; align-items: center;
  }
  .title-row { display: flex; gap: 6px; }
  .tile {
    width: 90px; height: 96px; display: flex; align-items: center; justify-content: center;
    font-family: "Graduate", serif; font-size: 78px; line-height: 1; color: var(--white);
    text-shadow: 2px 2px 0 rgba(0,0,0,0.35);
  }
  .tile--ink { background: var(--ink); }
  .tile--pink { background: var(--pink); }
  .tile--blue { background: var(--blue); }
  .tile--gap { width: 24px; background: transparent; }

  .tagline {
    position: absolute; left: 228px; top: 600px; width: 300px; padding: 16px 18px;
    background: var(--tag-bg);
    font-family: "Archivo", sans-serif; font-weight: 800; font-size: 25px; line-height: 1.25; color: var(--ink);
  }

  .still {
    position: absolute; border: 6px solid var(--ink); background: linear-gradient(160deg, #5c6f7d, #2e3a44);
  }
  .still--one { left: 541px; top: 596px; width: 152px; height: 178px; background: linear-gradient(160deg, #7a8c62, #3b3f3a); }
  .still--two { left: 703px; top: 596px; width: 152px; height: 178px; background: linear-gradient(160deg, #6f98b8, #2c3d6a); }
  .still--three { left: 541px; top: 790px; width: 152px; height: 184px; background: linear-gradient(160deg, #3f88c4, #b88a80); }

  .credits {
    position: absolute; right: 22px; top: 1010px; text-align: right;
    font-family: "Archivo", sans-serif; font-weight: 800; color: var(--ink);
  }
  .credits-label { font-size: 19px; margin-bottom: 4px; }
  .credits-name { font-size: 29px; line-height: 1.2; }

  .director {
    position: absolute; left: 392px; top: 1146px; width: 462px; height: 40px;
    background: var(--ink); color: var(--white);
    display: flex; align-items: center; gap: 10px; padding-left: 12px;
    font-family: "Archivo", sans-serif; font-weight: 800;
  }
  .director-label { font-size: 17px; }
  .director-name { font-size: 24px; }
</style>
</head>
<body>
<main class="poster">
  <svg class="collage" width="902" height="1200" viewBox="0 0 902 1200" xmlns="http://www.w3.org/2000/svg">
    <defs>
      <linearGradient id="scrapDark" x1="0" y1="0" x2="1" y2="1">
        <stop offset="0" stop-color="#7a2a1e"/><stop offset="0.4" stop-color="#161616"/><stop offset="1" stop-color="#2a2a2a"/>
      </linearGradient>
      <linearGradient id="lockerBlue" x1="0" y1="0" x2="1" y2="1">
        <stop offset="0" stop-color="#22346a"/><stop offset="1" stop-color="#4a67a8"/>
      </linearGradient>
      <linearGradient id="lockerSide" x1="0" y1="0" x2="1" y2="0">
        <stop offset="0" stop-color="#3b5c9c"/><stop offset="1" stop-color="#6a86c0"/>
      </linearGradient>
      <linearGradient id="wallPale" x1="0" y1="0" x2="1" y2="1">
        <stop offset="0" stop-color="#a9c4d9"/><stop offset="1" stop-color="#e8eef1"/>
      </linearGradient>
    </defs>
    <rect class="paper" width="902" height="1200" fill="#e4e8ea"/>
    <polygon role="img" aria-label="Torn wall paper with pale blue wash" fill="url(#wallPale)"
      points="300,760 902,700 902,1200 300,1200"/>
    <polygon role="img" aria-label="Torn poster scraps with graffiti lettering" fill="url(#scrapDark)"
      points="0,0 340,0 330,70 305,300 255,350 150,340 0,330"/>
    <polygon role="img" aria-label="Row of blue school lockers" fill="url(#lockerSide)"
      points="0,330 160,325 165,600 150,890 0,910"/>
    <polygon role="img" aria-label="Close view of blue school lockers" fill="url(#lockerBlue)"
      points="335,40 560,15 700,25 725,170 650,320 480,385 400,300 360,160"/>
    <polygon role="img" aria-label="Cooking show flyer with a kitchen knife" fill="#9a9444"
      points="30,720 320,650 345,1200 0,1200 0,820"/>
    <g font-family="'Over the Rainbow', cursive" font-size="30" fill="#bcd3ee" transform="rotate(-28 560 180)">
      <text x="470" y="130">the bully</text>
      <text x="455" y="175">the victim</text>
      <text x="440" y="220">the friends</text>
      <text x="425" y="265">the sparks</text>
    </g>
  </svg>

  <h1 class="title" aria-label="Hallway Sparks">
    <span class="title-row">
      <span class="tile tile--ink">H</span>
      <span class="tile tile--pink">A</span>
      <span class="tile tile--blue">L</span>
      <span class="tile tile--pink">L</span>
      <span class="tile tile--ink">W</span>
      <span class="tile tile--pink">A</span>
      <span class="tile tile--blue">Y</span>
    </span>
    <span class="title-row">
      <span class="tile tile--pink">S</span>
      <span class="tile tile--blue">P</span>
      <span class="tile tile--ink">A</span>
      <span class="tile tile--pink">R</span>
      <span class="tile tile--blue">K</span>
      <span class="tile tile--ink">S</span>
    </span>
  </h1>

  <p class="tagline">Forced to work alongside your school tormentor, what do you do?</p>

  <div class="still still--one" role="img" aria-label="Film still of a long-haired boy outdoors"></div>
  <div class="still still--two" role="img" aria-label="Film still of a boy in a red cap by the water"></div>
  <div class="still still--three" role="img" aria-label="Film still of a girl in a school hallway"></div>

  <section class="credits">
    <p class="credits-label">Cast</p>
    <p class="credits-name">MARA VELLOSO</p>
    <p class="credits-name">JONAH PRITCHETT</p>
    <p class="credits-name">ELLIS MARROW</p>
  </section>

  <p class="director"><span class="director-label">Director</span><span class="director-name">Daniel Reyes Hartwell</span></p>
</main>
</body>
</html>
```